VORK.
BRIDGING HORIZONS
VORK. -
Creative Brief
Use specific fonts
any thing which suits with the LOGO provided
Professional
RAJESH MOTLA
MR.
B.P. No.6213, COMMUNE-3, NEAR TORAVI LAUNDRY, KALEBA ZONE, BAMAKO-MALI
rajesh@vork.co.in
vork.co.in
pls mention MANAGING DIRECTOR, the designation, below the name of the person.
LOGO at centre. Below mentioned address at bottom: India Office D-47, Palm Enclave-II, Gurgaon, Haryana 122015 ph:+91-124-4708352, fax:+91-124-4519267 cell:+91-9871436029

```html
<!DOCTYPE html>
<html lang="en">
<head>
<meta charset="utf-8">
<title>VORK. – Business Cards</title>
<link rel="stylesheet" href="https://fonts.googleapis.com/css2?family=Exo+2:ital,wght@0,400;0,600;0,800;1,700&display=swap">
<style>
  :root{
    --page:#e9e7e4;
    --card:#ffffff;
    --navy:#1c2a6e;
    --blue:#1f5fa8;
    --teal:#1d9bb8;
    --green:#5aa82a;
    --ink:#4a4a4a;
    --muted:#6d6d6d;
    --badge-edge:#c9d3d9;
  }
  *{margin:0;padding:0;box-sizing:border-box}
  html,body{width:1200px;height:852px;overflow:hidden}
  body{background:var(--page);font-family:"Exo 2",Arial,sans-serif;position:relative}

  .card{position:absolute;width:520px;height:300px;background:var(--card);border-radius:18px;overflow:hidden;box-shadow:0 10px 26px rgba(0,0,0,.22)}
  .card--classic{left:70px;top:110px}
  .card--icons{left:610px;top:440px}

  .card__band{position:absolute;top:0;left:62px;width:44px;height:100%;
    background:linear-gradient(180deg,var(--navy) 0%,var(--blue) 30%,var(--teal) 60%,var(--blue) 85%,var(--navy) 100%)}
  .card__band::after{content:"";position:absolute;top:0;right:-6px;width:6px;height:100%;background:linear-gradient(180deg,#9ed3e4,#e4f3f8)}

  .brand{position:absolute;left:40px;top:34px;display:flex;align-items:center;gap:12px}
  .brand__dot{width:86px;height:86px;border-radius:50%;background:var(--navy);border:5px solid #fff;box-shadow:0 0 0 2px var(--teal)}
  .brand__name{font-weight:800;font-size:52px;line-height:1;color:var(--navy);letter-spacing:1px}
  .brand__tag{font-weight:600;font-size:13px;color:var(--green);letter-spacing:1.5px;margin-top:3px}

  .contact{position:absolute;left:150px;top:150px;font-size:11.5px;line-height:15px;color:var(--muted)}
  .contact__gap{height:9px}
  .contact__row{display:flex;align-items:center;gap:6px}
  .contact__row svg{width:12px;height:12px;fill:var(--navy)}

  .badge{position:absolute;right:18px;top:140px;width:170px;height:92px;border-radius:50%;
    background:radial-gradient(ellipse at 40% 35%,#ffffff 0%,#eef3f6 60%,#dbe4ea 100%);
    border:2px solid var(--badge-edge);display:flex;flex-direction:column;align-items:center;justify-content:center}
  .badge__name{font-weight:700;font-size:15px;color:var(--navy)}
  .badge__title{font-weight:700;font-style:italic;font-size:11.5px;color:#fff;background:var(--green);padding:1px 8px;border-radius:3px;margin-top:4px}

  .card--icons .contact{left:150px;top:140px}
  .band-icons{position:absolute;left:62px;width:44px;display:flex;flex-direction:column;align-items:center}
  .band-icons--home{top:142px}
  .band-icons--reach{top:212px;gap:7px}
  .band-icons svg{width:14px;height:14px;fill:#fff}
</style>
</head>
<body>

<section class="card card--classic" aria-label="Business card, classic layout">
  <div class="card__band"></div>
  <div class="brand">
    <div class="brand__dot"></div>
    <div>
      <div class="brand__name">VORK</div>
      <div class="brand__tag">BRIDGING HORIZONS</div>
    </div>
  </div>
  <address class="contact" style="font-style:normal">
    <div>B.P. No.6213, Commune-3,</div>
    <div>Near Toravi Laundry,</div>
    <div>Kaleba Zone, Bamako-Mali</div>
    <div class="contact__gap"></div>
    <div class="contact__row"><svg viewBox="0 0 24 24"><path d="M6.6 10.8a15 15 0 0 0 6.6 6.6l2.2-2.2a1 1 0 0 1 1-.25 11.4 11.4 0 0 0 3.6.57 1 1 0 0 1 1 1V20a1 1 0 0 1-1 1A17 17 0 0 1 3 4a1 1 0 0 1 1-1h3.5a1 1 0 0 1 1 1c0 1.25.2 2.45.57 3.6a1 1 0 0 1-.25 1z"/></svg>+223-20418365</div>
    <div class="contact__row"><svg viewBox="0 0 24 24"><rect x="6" y="2" width="12" height="20" rx="2"/></svg>+223-76293148</div>
    <div class="contact__row"><svg viewBox="0 0 24 24"><circle cx="12" cy="12" r="10"/></svg>rajesh@vork.co.in</div>
    <div class="contact__gap"></div>
    <div class="contact__row"><svg viewBox="0 0 24 24"><circle cx="12" cy="12" r="10"/></svg>www.vork.co.in</div>
  </address>
  <div class="badge">
    <div class="badge__name">Rajesh Motla</div>
    <div class="badge__title">Managing Director</div>
  </div>
</section>

<section class="card card--icons" aria-label="Business card, icon layout">
  <div class="card__band"></div>
  <div class="band-icons band-icons--home">
    <svg viewBox="0 0 24 24"><path d="M12 3 2 12h3v9h5v-6h4v6h5v-9h3z"/></svg>
  </div>
  <div class="band-icons band-icons--reach">
    <svg viewBox="0 0 24 24"><rect x="7" y="2" width="10" height="20" rx="2"/></svg>
    <svg viewBox="0 0 24 24"><path d="M2 5h20v14H2zm2 2v.5l8 5 8-5V7z"/></svg>
    <svg viewBox="0 0 24 24"><circle cx="12" cy="12" r="10"/></svg>
  </div>
  <div class="brand">
    <div class="brand__dot"></div>
    <div>
      <div class="brand__name">VORK</div>
      <div class="brand__tag">BRIDGING HORIZONS</div>
    </div>
  </div>
  <address class="contact" style="font-style:normal">
    <div>B.P. No.6213, Commune-3,</div>
    <div>Near Toravi Laundry,</div>
    <div>Kaleba Zone, Bamako-Mali</div>
    <div class="contact__gap"></div>
    <div>+223-20418365</div>
    <div>+223-76293148</div>
    <div>rajesh@vork.co.in</div>
    <div class="contact__gap"></div>
    <div>www.vork.co.in</div>
  </address>
  <div class="badge">
    <div class="badge__name">Rajesh Motla</div>
    <div class="badge__title">Managing Director</div>
  </div>
</section>

</body>
</html>
```